new banner sliders for our web site

We would like to replace and create new set of sliding banners (5-10, resolution 930x380) for the main page of our online store at http://www.velmorix.example/online. We are thinking about highlighting the main company's products and services categories as well as maybe some featured individual products with those banners on the product pages.

1: Long Range Wavelink® set of products showing off the super long range our our products as well as the capability to extend the range to normally 10m by factor 10 or more.
2: The product we have are used to connect industrial bar code scanners, GPS, land surveying instruments and other Wavelink devices to a PC and greater range.
3: You can use our products to connect Wavelink audio speakers to your PC or you can use e.g. the VELMORix Sonic QT to receive music from your smartphone to your home stereo system. Products can be used to connect keyboard/mouse in a home theater system, where the PC is in the basement, e.g.
4: A new category products is based on the Wavelink Lite® standard. Making WLE (Wavelink Low Energy) long range is unique. The products can be used for uPulse transmission at higher power, the biggest in industry (MegaPing) or it can be used to receive uPulse transmissions, even relaying them. uPulses are used for proximity marketing advertisement, allowing stores to reach more customers.
5: Long range WLE must be used to get data from heart rate sensors in a gym setting e.g. where you have a number of people wearing those in a large room. It could be a football game where players wear WLE sensors.
6: we have a set of Wavelink to Serial products that can be highlighted in a banner: standard Wavelink: Trunk7, Trunk7Q, Mini and Wavelink Lite: KeenPico
7: another banner should highlight that all our products are build with our own Wavelink modules (VELMORix SMD, VELMORix BLE). We are also offering custom product design and firmware development to meet customer's need. We know how to make modules and we can make one for you at any size and with any type of sensor attached to it.
8: last is a product we are developing for the home automation industry. We started with a web page at http://www.glowtuner.example, username velmorix password velmorix. A single banner that matches the other designs would be nice. This is an "available soon" product.

If you come up with other ideas how to highlight our products and services, we would be grateful and you have the winning bid.

Thank you very much
Torvald

Target Market(s)

The market for long range Wavelink products is mostly industrial or B2B. E.g. our products are used with industrial sensors like barcode scanners in a warehouse or survey instruments in the field. They are also used by marketing companies who engage in the new uPulse technology to reach customers at a greater instance.
Some customers are home automation companies or home theatre installers for long range mouse/keyboard connections or audio receiver at home stereo systems.
Our products are seldom used by the average consumer.

Industry/Entity Type

Industrial

Requirements
Must have
• The banner design should visualize the use cases of our products. We'd like to see one or more banners for each use case that visualize:
1: long range capability, featuring Base QT or MegaPing
2: industrial serial to computer connections, featuring Trunk7(Q) and KeenPico
3: proximity marketing, featuring KeenPing and MegaPing
4: custom design service, featuring VELMORixSMD and VELMORixBLE
5: home automation, featuring GlowTuner, GlowSocket
6: home theatre, featuring Base QT and Sonic QT
Nice to have
• Parallax and responsive
Should not have
• too much consumer oriented product presentation

```html
<!DOCTYPE html>
<html lang="en">
<head>
<meta charset="utf-8">
<title>Products Available Soon</title>
<link rel="stylesheet" href="https://fonts.googleapis.com/css2?family=Raleway:wght@500;600&display=swap">
<style>
  :root {
    --blue-deep: #0a3f8f;
    --blue-mid: #0d5aa8;
    --blue-bright: #0b72c2;
    --blue-accent: #5e9fdf;
    --white: #ffffff;
    --paper: #f5f6f8;
    --label: #7d838a;
    --metal-light: #eceef0;
    --metal-mid: #c9cdd1;
    --metal-dark: #8e9398;
    --shadow: rgba(40, 50, 60, 0.28);
  }
  html, body {
    margin: 0;
    padding: 0;
    width: 1200px;
    height: 490px;
    overflow: hidden;
    background: var(--white);
  }
  .banner {
    position: relative;
    width: 1200px;
    height: 490px;
    overflow: hidden;
    font-family: "Raleway", Arial, sans-serif;
  }
  .banner-backdrop {
    position: absolute;
    inset: 0;
    display: block;
  }
  .banner-headline {
    position: absolute;
    left: 82px;
    top: 178px;
    margin: 0;
    color: var(--white);
    font-weight: 500;
    font-size: 38px;
    line-height: 55px;
    letter-spacing: 0.1px;
  }
  .product-visual {
    position: absolute;
    left: 748px;
    top: 150px;
    width: 330px;
    height: 170px;
    border-radius: 34px 60px 30px 40px;
    transform: rotate(-11deg) skewX(-14deg);
    background:
      linear-gradient(160deg, var(--metal-light) 0%, var(--metal-mid) 55%, var(--metal-dark) 100%);
    box-shadow: 0 18px 26px -10px var(--shadow);
  }
  .slide-code {
    position: absolute;
    right: 9px;
    bottom: 7px;
    color: var(--label);
    font-size: 14px;
    font-weight: 500;
    font-variant-numeric: lining-nums;
  }
</style>
</head>
<body>
  <section class="banner">
    <svg class="banner-backdrop" width="1200" height="490" viewBox="0 0 1200 490" aria-hidden="true">
      <defs>
        <linearGradient id="blue-field" x1="0" y1="0" x2="0.6" y2="1">
          <stop offset="0" stop-color="#0b72c2"/>
          <stop offset="0.55" stop-color="#0d5aa8"/>
          <stop offset="1" stop-color="#0a3f8f"/>
        </linearGradient>
        <linearGradient id="white-field" x1="0" y1="0" x2="1" y2="0">
          <stop offset="0" stop-color="#ffffff"/>
          <stop offset="1" stop-color="#f5f6f8"/>
        </linearGradient>
      </defs>
      <rect width="1200" height="490" fill="url(#blue-field)"/>
      <path class="accent-arc" d="M560 0 C440 120 430 360 600 490 L1200 490 L1200 0 Z" fill="#5e9fdf"/>
      <path class="white-arc" d="M582 0 C460 120 420 340 700 490 L1200 490 L1200 0 Z" fill="url(#white-field)"/>
    </svg>

    <h1 class="banner-headline">Products<br>Available Soon</h1>

    <div class="product-visual" role="img" aria-label="Product photo: brushed-aluminium wireless adapter with antenna and mounting bracket"></div>

    <span class="slide-code">X14</span>
  </section>
</body>
</html>
```